Medical Marijuana Service in the Bay Area

This is for a business card design that is going to be making medical marijuana deliveries in the bay area. The name of the the business is "Coastal Sage Wellness". I would like to have a modern feel and showing us as a medical marijuana company but at the same time discrete about it. I'm trying to target more sophisticated clients.

Industry/Entity Type

Medical

Contact Information for Business Card

Would like people to know it is for medical marijuana but in a discrete way.

```html
<!DOCTYPE html>
<html lang="en">
<head>
<meta charset="utf-8">
<title>Coastal Sage Wellness – Business Card</title>
<link href="https://fonts.googleapis.com/css2?family=Poiret+One&family=PT+Sans+Narrow&display=swap" rel="stylesheet">
<style>
  :root {
    --page-bg: #ffffff;
    --card-bg: #ffffff;
    --card-edge: #d6d6d6;
    --ink-name: #5a5a5a;
    --ink-contact: #666666;
    --mark-yellow: #e4ea8c;
    --mark-teal: #3fa3bd;
  }
  html, body {
    margin: 0;
    padding: 0;
    width: 1200px;
    height: 849px;
    overflow: hidden;
    background: var(--page-bg);
  }
  .canvas {
    position: relative;
    width: 1200px;
    height: 849px;
  }
  .business-card {
    position: absolute;
    left: 432px;
    top: 320px;
    width: 360px;
    height: 205px;
    box-sizing: border-box;
    background: var(--card-bg);
    border: 1px solid var(--card-edge);
    text-align: center;
  }
  .brand-mark {
    position: absolute;
    left: 135px;
    top: 13px;
    width: 90px;
    height: 90px;
  }
  .brand-name {
    position: absolute;
    left: 0;
    right: 0;
    top: 110px;
    margin: 0;
    font-family: "Poiret One", sans-serif;
    font-weight: 400;
    font-size: 20px;
    letter-spacing: 0.2px;
    color: var(--ink-name);
  }
  .contact {
    position: absolute;
    left: 0;
    right: 0;
    top: 161px;
    margin: 0;
    font-family: "PT Sans Narrow", sans-serif;
    font-size: 12px;
    line-height: 15px;
    color: var(--ink-contact);
    font-style: normal;
  }
  .contact span { display: block; }
</style>
</head>
<body>
  <main class="canvas">
    <section class="business-card">
      <svg class="brand-mark" viewBox="0 0 90 90" role="img" aria-label="Soft yellow-to-teal brand circle">
        <defs>
          <linearGradient id="markTone" x1="0" y1="0.6" x2="1" y2="0.3">
            <stop offset="0" stop-color="var(--mark-yellow)"/>
            <stop offset="1" stop-color="var(--mark-teal)"/>
          </linearGradient>
        </defs>
        <circle cx="45" cy="45" r="45" fill="url(#markTone)"/>
      </svg>
      <h1 class="brand-name">Coastal Sage Wellness</h1>
      <address class="contact">
        <span class="contact-phone">415-555-0148</span>
        <span class="contact-email">hello@coastalsagewellness.com</span>
      </address>
    </section>
  </main>
</body>
</html>
```